Box Design for Concrete Mixer Truck Parts

Overview:
KVSUPPLY, a trusted supplier of concrete mixer, heavy-duty truck, and batch plant parts, is seeking a creative and professional packaging design for boxes that will contain concrete mixer truck parts. The design should reflect our brand identity while ensuring practicality and visual appeal.

Design Requirements:

Branding: The box must prominently feature the KVSUPPLY logo (attached).
Part Number Area: Include a designated space where part number stickers can be applied.
Color Scheme: The design should incorporate red as a primary color and may include up to three colors in total.
Style: The box should have a slick, modern, and creative design that aligns with our industry and brand.
Functionality: The design should be visually appealing while maintaining a professional and industrial feel, suitable for heavy-duty truck parts packaging.

We've included the box template and an example of a box using this template to help with orientation.

```html
<!DOCTYPE html>
<html lang="en">
<head>
<meta charset="utf-8">
<title>KVSUPPLY Parts Box</title>
<link rel="stylesheet" href="https://fonts.googleapis.com/css2?family=Oswald:wght@400;700&family=Montserrat:wght@600&display=swap">
<style>
  :root {
    --red: #d4182b;
    --red-deep: #b80d1d;
    --charcoal: #2e302f;
    --panel: #f3f3f4;
    --panel-edge: #dcdcde;
    --stage: #e6e7e9;
    --art-dark: #4a4c4c;
    --art-light: #d9dadb;
  }
  html, body {
    margin: 0;
    padding: 0;
    width: 1200px;
    height: 918px;
    overflow: hidden;
    background: var(--stage);
  }
  .box-flat {
    display: block;
    width: 1200px;
    height: 918px;
  }
  .brand-name {
    font-family: 'Oswald', sans-serif;
    font-weight: 700;
    fill: var(--charcoal);
    letter-spacing: 1px;
  }
  .brand-sub {
    font-family: 'Oswald', sans-serif;
    font-weight: 400;
    fill: var(--charcoal);
  }
  .site-url {
    font-family: 'Montserrat', sans-serif;
    font-weight: 600;
    fill: #ffffff;
    font-size: 14px;
    letter-spacing: 0.5px;
  }
  .panel-face { fill: var(--panel); stroke: var(--panel-edge); stroke-width: 1; }
  .band-red { fill: var(--red); }
  .band-red-deep { fill: var(--red-deep); }
  .band-dark { fill: var(--charcoal); }
  .brand-mark { fill: var(--red); }
  .brand-rule { stroke: var(--charcoal); stroke-width: 3; }
  .sticker-area { fill: #ffffff; stroke: #7b7c7e; stroke-width: 1.2; }
</style>
</head>
<body>
<svg class="box-flat" viewBox="0 0 1200 918" xmlns="http://www.w3.org/2000/svg">
  <defs>
    <linearGradient id="artTone" x1="0" y1="0" x2="1" y2="0">
      <stop offset="0" stop-color="var(--art-dark)"/>
      <stop offset="1" stop-color="var(--art-light)"/>
    </linearGradient>
  </defs>

  <!-- Top lid panel -->
  <g class="panel-top" transform="translate(560,60)">
    <rect class="panel-face" width="600" height="230"/>
    <polygon class="band-red" points="0,0 260,0 0,40"/>
    <polygon class="band-red-deep" points="0,190 0,230 220,230"/>
    <rect class="brand-mark" x="150" y="92" width="34" height="34"/>
    <text class="brand-name" x="196" y="122" font-size="38">KVSUPPLY</text>
    <text class="brand-sub" x="198" y="146" font-size="16">KV HEAVY PARTS SUPPLY CO, LLC</text>
  </g>

  <!-- Side panel -->
  <g class="panel-side" transform="translate(90,300)">
    <rect class="panel-face" width="460" height="560"/>
    <polygon class="band-red" points="0,0 460,0 460,50 170,0 0,20"/>
    <polygon class="band-red" points="0,330 0,560 200,560"/>
    <polygon class="band-dark" points="90,470 460,440 460,560 200,560"/>
    <rect class="brand-mark" x="60" y="70" width="46" height="46"/>
    <text class="brand-name" x="118" y="110" font-size="44">KVSUPPLY</text>
    <line class="brand-rule" x1="118" y1="124" x2="380" y2="124"/>
    <text class="brand-sub" x="118" y="148" font-size="20">KV HEAVY PARTS SUPPLY CO, LLC</text>
    <rect class="sticker-area" x="60" y="190" width="310" height="190" rx="12"/>
    <text class="site-url" x="24" y="540">www.kvsupply-parts.com</text>
  </g>

  <!-- Front panel -->
  <g class="panel-front" transform="translate(560,300)">
    <rect class="panel-face" width="600" height="560"/>
    <polygon class="band-red" points="0,0 600,0 380,20 0,70"/>
    <polygon class="band-dark" points="0,470 430,455 260,560 0,560"/>
    <polygon class="band-red-deep" points="600,400 600,560 260,560"/>
    <rect class="brand-mark" x="70" y="110" width="54" height="54"/>
    <text class="brand-name" x="138" y="156" font-size="54">KVSUPPLY</text>
    <line class="brand-rule" x1="138" y1="172" x2="520" y2="172"/>
    <text class="brand-sub" x="138" y="200" font-size="24">KV HEAVY PARTS SUPPLY CO, LLC</text>
    <rect x="70" y="240" width="460" height="210" fill="url(#artTone)" role="img" aria-label="Line illustration of a concrete mixer truck beside a concrete batch plant"/>
    <text class="site-url" x="400" y="535">www.kvsupply-parts.com</text>
  </g>
</svg>
</body>
</html>
```